Brightvale Copackaging Website using Wix Platform

Project Overview:
Brightvale Copackaging is a supply chain company specializing in packaging and manufacturing services for CPG (Consumer Packaged Goods) brands and nutritional/dietary supplement companies. The company offers end-to-end solutions including packaging design, production, co-packing, and private labeling. The goal of this project is to create a professional, user-friendly website that showcases your expertise, builds trust with potential clients, and generates leads for your services.

Objectives:
Establish Brand Authority: Position Brightvale Copackaging as a leader in the packaging and manufacturing industry for CPG and nutritional products.
Lead Generation: Encourage visitors to contact you for quotes, consultations, or further information.
Professional User Experience: Ensure the website is easy to navigate, visually appealing, and mobile-friendly.
SEO & Conversion Optimization: Optimize the site for search engines to attract organic traffic and improve conversion rates.
Primary Audience:
CPG Brands: Companies in industries like food and beverage, personal care, and household products looking for packaging and manufacturing services.
Nutritional/Dietary Supplement Brands: Companies in the health and wellness industry needing specialized packaging and manufacturing services for supplements, including compliance with regulatory standards (GMP).
Secondary Audience:
Potential partners looking to collaborate on co-packing or private labeling.
Key Features & Functionality:
Responsive Design:

The website must be fully responsive, ensuring optimal viewing across all devices (desktops, tablets, mobile).
User-Centric Navigation:

A clean, intuitive navigation system that allows users to quickly access key pages such as Home, Services, About Us, Case Studies, FAQ, and Contact.
Lead Generation Forms:

Prominent CTAs (Calls to Action) throughout the website encouraging users to “Request a Quote”, “Get in Touch”, or “Learn More” about your services.
Contact Form: Simple form allowing potential clients to submit inquiries about your services.
SEO Optimization:

The site should be optimized for relevant keywords (e.g., “co-packing services for CPG,” “nutritional supplement packaging,” “custom packaging solutions”), including meta descriptions, headers, and on-page content.
Content Management System (CMS):

An easy-to-use CMS (like WordPress or Webflow) for easy content updates. This will allow you to make changes to your services, case studies, and other sections without requiring a developer.
Analytics Integration:

Google Analytics or a similar tool for tracking site visitors and performance metrics to make data-driven decisions on site improvements.
Site Structure & Content:
1. Home Page:
Hero Section with tagline, images or video of your services in action, and a clear CTA (e.g., “Request a Quote”).
Value Proposition: Short and compelling introduction to Brightvale Copackaging’s core services and advantages.
Overview of Services: Highlight your key offerings (e.g., Packaging Design, Co-packing, Nutritional Supplement Packaging, Private Labeling).
Client Logos/Testimonials: Social proof to establish credibility.
CTA Buttons: Throughout the page to drive conversions (e.g., “Get a Free Consultation”).
2. About Us Page:
Company Overview: Explain your mission, values, and commitment to quality.
Team Overview (Optional): Introduce key team members to humanize your company and build trust.
Core Values and Differentiators: Showcase what makes Brightvale Copackaging unique—sustainability practices, regulatory compliance, and industry expertise.
3. Services Pages (Separate Pages for Each Service):
Packaging & Design: Custom packaging solutions, materials, and design services for CPG brands.
Manufacturing & Assembly: Your end-to-end production process, assembly capabilities, and how you support both small and large-scale runs.
Nutritional & Dietary Supplement Packaging: Focus on specialized packaging for supplements, regulatory compliance (GMP), and certifications.
Private Labeling: Services for clients who wish to brand their own products using your packaging.
Each service page will include detailed descriptions, benefits, process information, and CTAs like “Get Started” or “Request a Quote”.
4. Case Studies / Portfolio Page:
Success Stories: Showcase in-depth case studies of past projects, especially successful partnerships with CPG or supplement brands.
Before & After Images: Display the difference your services have made for clients, especially in terms of packaging quality or branding improvements.
Client Testimonials: Additional customer feedback to strengthen your brand reputation.
5. FAQ Page:
Address common questions related to lead times, regulatory compliance, order quantities, and specific details for different industries (e.g., dietary supplements).
The format will be accordion-style or dropdowns for easy scanning.
6. Contact Us Page:
Contact Form: With fields for name, email, company, and inquiry details.
Location Information: Physical address, phone number, and working hours.
Map Integration: If relevant, integrate Google Maps to show your office location.
Social Media Links: Link to your company’s LinkedIn, Instagram, or other relevant platforms.

Target Market(s)

Startup CPG Brands, Supplement Brands, Nutrition Brands

Industry/Entity Type

Flexible Packaging, Contract Manufacturing, Supplement & Food Manufacturing

Requirements
Must have
• Use our colors.
Nice to have
• https://example-site.net/brightvalecopackaging - www.tarnwick.com - www.plumrossfoods.com - thebluegarner.co

```html
<!DOCTYPE html>
<html lang="en">
<head>
<meta charset="utf-8">
<title>Brightvale Copackaging</title>
<link rel="stylesheet" href="https://fonts.googleapis.com/css2?family=Outfit:wght@300;400;500;600;700&display=swap">
<style>
:root{
  --navy:#111f4d;
  --blue:#0ba4e2;
  --green:#a5c93a;
  --ink:#2b2b2b;
  --white:#fff;
}
*{box-sizing:border-box;margin:0;padding:0}
html,body{width:1200px;height:3274px;overflow:hidden}
body{font-family:'Outfit',sans-serif;color:var(--ink);background:var(--white);position:relative}
.abs{position:absolute}
.btn{position:absolute;display:flex;align-items:center;justify-content:center;color:#fff;font-size:14px;font-weight:500;text-transform:uppercase;letter-spacing:.2px}
.btn-blue{background:var(--blue)}
.btn-green{background:var(--green)}
/* header */
.site-header{top:0;left:0;width:1200px;height:86px;background:var(--navy)}
.brand{position:absolute;display:flex;align-items:center;color:#fff;font-weight:400;letter-spacing:.3px;white-space:nowrap}
.brand-dot{width:16px;height:16px;border-radius:50%;background:var(--blue);margin-right:9px;flex:none}
.brand-rule{width:1px;background:#fff;opacity:.8;margin-right:9px;flex:none}
.main-nav{position:absolute;top:33px;left:455px;display:flex;gap:34px;font-size:14.5px;font-weight:500;color:#fff;white-space:nowrap}
.main-nav .active{color:var(--green);position:relative}
.main-nav .active::after{content:"";position:absolute;left:0;right:0;top:24px;height:2px;background:var(--green)}
/* hero */
.hero-media{top:86px;left:0;width:1200px;height:471px;background:linear-gradient(100deg,#4e4e4e 0%,#6a6866 45%,#8d8780 65%,#55524f 100%)}
.hero-media::after{content:"";position:absolute;right:140px;top:50px;width:430px;height:380px;background:linear-gradient(90deg,#5b534a 0 48%,#d8ccba 48% 100%);opacity:.55;border-radius:6px}
.hero-title{top:176px;left:112px;width:500px;font-size:39px;font-weight:700;line-height:48px;color:#fff;text-transform:uppercase}
.hero-title span{color:var(--blue)}
.hero-text{top:340px;left:112px;width:462px;font-size:17px;line-height:26px;color:#fff;text-align:justify}
.slide-arrow{position:absolute;top:290px;width:45px;height:64px;background:#fff;display:flex;align-items:center;justify-content:center}
/* titles */
.section-title{position:absolute;left:0;width:1200px;text-align:center;font-size:38px;font-weight:700;text-transform:uppercase}
.section-title .a{color:var(--blue)} .section-title .b{color:var(--green)}
.title-rule{position:absolute;left:550px;width:100px;height:3px;background:var(--navy)}
/* expertise */
.service-card{position:absolute;top:747px;width:297px;height:283px}
.service-card .media{width:297px;height:260px}
.service-card .label{position:absolute;left:22px;top:237px;width:253px;height:46px;background:#fff;box-shadow:0 2px 6px rgba(0,0,0,.18);display:flex;align-items:center;justify-content:center;font-size:20px;font-weight:500;text-transform:uppercase;color:#222}
/* about */
.about-band{top:1205px;left:0;width:1200px;height:575px;background:var(--green)}
.about-photo{top:1291px;left:112px;width:423px;height:402px;background:linear-gradient(180deg,#d9d1c3 0%,#cdb88f 55%,#b8955e 100%)}
.about-bar{top:1330px;left:535px;width:30px;height:325px;background:var(--blue)}
.about-title{top:1298px;left:634px;font-size:38px;font-weight:700;color:#fff}
.about-rule{top:1355px;left:634px;width:100px;height:3px;background:#fff}
.about-text{left:634px;width:454px;font-size:17px;line-height:24px;color:#fff;text-align:justify}
/* testimonials */
.testi-card{position:absolute;top:1968px;width:463px;height:273px;border:2px solid #e4e4e4;border-radius:14px;box-shadow:0 3px 8px rgba(0,0,0,.12);background:#fff}
.testi-card p{position:absolute;left:28px;top:28px;width:406px;font-size:13.4px;line-height:21.5px;color:#333;text-align:justify}
.testi-foot{position:absolute;left:30px;top:168px;height:85px;border-left:2px solid var(--green);padding-left:14px;display:flex;align-items:center}
.avatar{width:74px;height:74px;border-radius:50%;background:linear-gradient(160deg,#c9d6e3,#8ea9c2)}
.person{margin-left:10px}
.stars{color:#f2a516;font-size:15px;letter-spacing:1px}
.person b{display:block;font-size:19px;font-weight:500;color:#222}
.client-name{position:absolute;right:28px;top:200px;font-size:17px;font-weight:600;color:#111;display:flex;align-items:center;gap:7px}
.client-name i{width:14px;height:14px;background:#111;display:block}
.testi-arrow{position:absolute;top:2094px}
/* contact */
.contact-band{top:2330px;left:0;width:1200px;height:658px;background:linear-gradient(180deg,#a8cd31,#b1d23f 50%,#a3c72e)}
.contact-title{top:2410px;left:0;width:1200px;text-align:center;font-size:38px;font-weight:700;color:#fff}
.contact-rule{top:2466px;left:550px;width:100px;height:3px;background:#fff}
.contact-form{top:2510px;left:112px;width:976px;height:390px;background:#fff;border-radius:18px}
.field{position:absolute;border:1px solid #555;font-size:14.5px;color:#333;padding:10px 17px}
/* footer */
.site-footer{top:2988px;left:0;width:1200px;height:286px;background:var(--navy);color:#fff}
.foot-info{position:absolute;top:3116px;left:0;width:1200px;display:flex;justify-content:center;gap:22px;font-size:14.5px;align-items:center;color:#fff}
.foot-info span{display:flex;align-items:center;gap:6px}
.foot-sep{width:1px;height:22px;background:#fff}
.foot-nav{position:absolute;top:3160px;left:0;width:1200px;display:flex;justify-content:center;gap:42px;font-size:19px;font-weight:500;color:#fff}
.foot-rule{position:absolute;top:3206px;left:112px;width:976px;height:1px;background:#6a7596}
.copyright{position:absolute;top:3226px;left:112px;font-size:14px;color:#d8dbe6}
.follow{position:absolute;top:3220px;left:816px;display:flex;align-items:center;gap:7px;font-size:18px;color:#fff}
.follow i{display:block;width:26px;height:26px;border:1.5px solid #fff;border-radius:50%}
</style>
</head>
<body>

<header class="abs site-header">
  <div class="brand" style="top:27px;left:112px;font-size:20px">
    <span class="brand-dot"></span><span class="brand-rule" style="height:30px"></span>BRIGHTVALE COPACKAGING
  </div>
  <nav class="main-nav">
    <span class="active">HOME</span><span>ABOUT US</span><span>SERVICES</span><span>CASE STUDIES</span><span>FAQS</span>
  </nav>
  <div class="btn btn-blue" style="top:25px;left:966px;width:122px;height:35px">Contact Us</div>
</header>

<section>
  <div class="abs hero-media" role="img" aria-label="Two stand-up packaging pouches on boxes"></div>
  <h1 class="abs hero-title">End-to-end <span>packaging solutions</span> for CPG &amp; nutritional products</h1>
  <p class="abs hero-text">We deliver high-quality packaging and manufacturing services tailored to your brand's needs.</p>
  <div class="btn btn-green" style="top:407px;left:112px;width:175px;height:37px">Request a Quote</div>
  <div class="btn btn-blue" style="top:407px;left:310px;width:159px;height:37px">Learn More</div>
  <div class="slide-arrow" style="left:0"><svg width="14" height="20"><path d="M11 2 3 10l8 8" stroke="#111" stroke-width="2.5" fill="none"/></svg></div>
  <div class="slide-arrow" style="left:1155px"><svg width="14" height="20"><path d="M3 2l8 8-8 8" stroke="#111" stroke-width="2.5" fill="none"/></svg></div>
</section>

<section>
  <h2 class="section-title" style="top:636px"><span class="a">Our</span> <span class="b">Expertise</span></h2>
  <div class="title-rule" style="top:693px"></div>
  <div class="service-card" style="left:112px">
    <div class="media" role="img" aria-label="Designer sketching packaging boxes" style="background:linear-gradient(135deg,#d8d4cd,#b79f80)"></div>
    <div class="label">Packaging Design</div>
  </div>
  <div class="service-card" style="left:452px">
    <div class="media" role="img" aria-label="Printed snack pouches" style="background:linear-gradient(135deg,#1d7a7c,#2f9a95 60%,#e4e6e6)"></div>
    <div class="label">Co-Packing</div>
  </div>
  <div class="service-card" style="left:792px">
    <div class="media" role="img" aria-label="Plain label-ready pouch" style="background:linear-gradient(180deg,#ececec,#dfe9ef 60%,#9ad4e7)"></div>
    <div class="label">Private Labeling</div>
  </div>
  <div class="btn btn-blue" style="top:1078px;left:531px;width:139px;height:36px">View More</div>
</section>

<section>
  <div class="abs about-band"></div>
  <div class="abs about-photo" role="img" aria-label="Gold pouch on a wooden kitchen counter"></div>
  <div class="abs about-bar"></div>
  <h2 class="abs about-title">ABOUT US</h2>
  <div class="abs about-rule"></div>
  <p class="abs about-text" style="top:1390px">Sed ut perspiciatis unde omnis iste natus error sit voluptatem accusantium doloremque laudantium, totam rem aperiam, eaque ipsa quae ab illo inventore veritatis et quasi architecto beatae vitae dicta sunt explicabo nemo enim ipsam voluptatem quia voluptas sit aspernatur aut odit aut fugit,</p>
  <p class="abs about-text" style="top:1552px">Sed ut perspiciatis unde omnis iste natus error sit voluptatem accusantium doloremque laudantium, totam rem aperiam, eaque ipsa quae ab</p>
  <div class="btn btn-blue" style="top:1641px;left:634px;width:160px;height:36px">Learn More</div>
</section>

<section>
  <h2 class="section-title" style="top:1857px"><span class="a">Client</span> <span class="b">Testimonials</span></h2>
  <div class="title-rule" style="top:1914px"></div>
  <svg class="testi-arrow" style="left:58px" width="14" height="22"><path d="M11 2 3 11l8 9" stroke="#111" stroke-width="2.5" fill="none"/></svg>
  <svg class="testi-arrow" style="left:1128px" width="14" height="22"><path d="M3 2l8 9-8 9" stroke="#111" stroke-width="2.5" fill="none"/></svg>
  <article class="testi-card" style="left:112px">
    <p>Lorem ipsum dolor sit amet, consectetur adipiscing elit, sed do eiusmod tempor incididunt ut labore et dolore magna aliqua. Ut enim ad minim veniam, quis nostrud exercitation ullamco laboris nisi ut aliquip ex ea commodo consequat. Duis aute irure dolor in reprehenderit in voluptate velit esse cillum dolore eu fugiat nulla pariatur.</p>
    <div class="testi-foot"><div class="avatar" role="img" aria-label="Client portrait"></div><div class="person"><div class="stars">★★★★☆</div><b>Daniel Reyes</b></div></div>
    <div class="client-name"><i></i>Kestrel Foods</div>
  </article>
  <article class="testi-card" style="left:628px">
    <p>Lorem ipsum dolor sit amet, consectetur adipiscing elit, sed do eiusmod tempor incididunt ut labore et dolore magna aliqua. Ut enim ad minim veniam, quis nostrud exercitation ullamco laboris nisi ut aliquip ex ea commodo consequat. Duis aute irure dolor in reprehenderit in voluptate velit esse cillum dolore eu fugiat nulla pariatur.</p>
    <div class="testi-foot"><div class="avatar" role="img" aria-label="Client portrait"></div><div class="person"><div class="stars">★★★★☆</div><b>Marcus Hale</b></div></div>
    <div class="client-name"><i></i>Juniper Labs</div>
  </article>
</section>

<section>
  <div class="abs contact-band" role="img" aria-label="Row of green pouches as backdrop"></div>
  <h2 class="abs contact-title">CONTACT US</h2>
  <div class="abs contact-rule"></div>
  <form class="abs contact-form">
    <div class="field" style="left:57px;top:37px;width:415px;height:37px">First Name</div>
    <div class="field" style="left:504px;top:37px;width:415px;height:37px">Last Name</div>
    <div class="field" style="left:57px;top:102px;width:415px;height:37px">Email Address</div>
    <div class="field" style="left:504px;top:102px;width:415px;height:37px">Phone Number</div>
    <div class="field" style="left:57px;top:167px;width:862px;height:123px">Message Us</div>
    <div class="btn btn-blue" style="left:374px;top:326px;width:229px;height:36px">Get a Free Consultation</div>
  </form>
</section>

<footer class="abs site-footer">
  <div class="brand" style="top:58px;left:0;width:1200px;justify-content:center;font-size:42px">
    <span class="brand-dot" style="width:22px;height:22px"></span><span class="brand-rule" style="height:58px"></span>BRIGHTVALE COPACKAGING
  </div>
</footer>
<div class="foot-info">
  <span><svg width="12" height="16"><path d="M6 1a5 5 0 0 0-5 5c0 4 5 9 5 9s5-5 5-9a5 5 0 0 0-5-5z" fill="#a5c93a"/><circle cx="6" cy="6" r="2" fill="#111f4d"/></svg>Nemo enim ipsam volupta</span>
  <i class="foot-sep"></i>
  <span><svg width="14" height="14"><path d="M3 1l3 3-2 2c1 2 2 3 4 4l2-2 3 3-2 2C6 13 1 8 1 3z" fill="#a5c93a"/></svg>+1 555 0142 7788</span>
  <i class="foot-sep"></i>
  <span><svg width="15" height="15"><circle cx="7.5" cy="7.5" r="7" fill="#a5c93a"/><path d="M7.5 3.5v4l3 2" stroke="#111f4d" stroke-width="1.5" fill="none"/></svg>Mon -Sat 9am - 7pm</span>
</div>
<nav class="foot-nav"><span>HOME</span><span>ABOUT US</span><span>SERVICES</span><span>CASE STUDIES</span><span>FAQS</span><span>CONTACT US</span></nav>
<div class="foot-rule"></div>
<div class="copyright">Copyright © 2024 Copackaging. All rights reserved.</div>
<div class="follow"><span style="margin-right:14px">FOLLOW US</span><i></i><i></i><i></i><i></i><i></i></div>

</body>
</html>
```